Velanza Reggaeton Night

I'd like to create a flyer / poster for a reaggaeton Xmas party in London. The party will be titled "Velanza" and will be VIP for friends of friends only. The concept has to remain classy and stylish as I don't want it to be related to anything tropical at first glance. People attending the party will be a bit up-scale so the style is key. I am thinking of a black background and golden or silver letters, which give a bit of a "bling" look. Since the party will take place in Central London, I was thinking perhaps including something that relates to the city (Holbrine Cathedral, the Quillet, etc.). I have seen a few ideas and I am happy to send those over to illustrate a bit better what I am thinking of. Color wise, the theme could be very black and grey (for the London buildings) and only keep a few bright red colors if including London double decker buses or phone booths. Need to include something that gives the poster / flyer a Latin vibe as well.

Target Market(s)

25-35 year olds. Young professionals living in London. Latin American and European origins. People that enjoy dancing and like reggaeton music in particular.

Industry/Entity Type

Latin American Café

Requirements
Must have
• Must have the name of the party, VELANZA, as a big part of the flyer. Also the words "reggaeton party" or "reggaeton night". Something catchy. The date will be December 16 2017. Time will be 7pm to 3am. Location is Central London (Bank). I don't want to specify the location as I want it to be "secret" and only people with the ticket will be given the address.
Nice to have
• Nice to have something that resembles London but also the Latin, bling vibe of reggaeton music. Velanza means "flirt" in Spanish so I want the design to be flirty but elegant and very stylish. VELANZA could be written in Gold or Silver to make it stand-out. Could be made up of yellow light bulbs as well. And could include a rose to make it more flirty. See examples attached.
Should not have
• Typical tropical or Cuban type designs. I don't want anything too colorful as I want to keep it classy and stylish. Try to avoid people dancing in the flyer. Don't want a photo of sexy women in the flyer. Need to keep it classy.

```html
<!DOCTYPE html>
<html lang="en">
<head>
<meta charset="utf-8">
<title>Velanza Reggaeton Night</title>
<link rel="stylesheet" href="https://fonts.googleapis.com/css2?family=Anton&family=Kelly+Slab&family=Share+Tech+Mono&display=swap">
<style>
  :root {
    --backdrop: #d6d6d6;
    --flyer-black: #111111;
    --flyer-grey: #3c3c3c;
    --flyer-mid: #262626;
    --gold: #ffc400;
    --rose-red: #c8101a;
    --rose-dark: #5e0208;
  }
  html, body {
    margin: 0;
    width: 1200px;
    height: 848px;
    overflow: hidden;
    background: var(--backdrop);
  }
  .flyer {
    position: absolute;
    left: 210px;
    top: 24px;
    width: 780px;
    height: 800px;
    background: var(--flyer-black);
    overflow: hidden;
    box-shadow: 0 10px 30px rgba(0,0,0,0.25);
  }
  .flyer__backdrop-photo {
    position: absolute;
    inset: 0;
    background:
      radial-gradient(circle at 82% 22%, rgba(110,110,110,0.30) 0, rgba(80,80,80,0.18) 18%, transparent 19%),
      radial-gradient(ellipse at 75% 45%, rgba(70,70,70,0.45) 0, transparent 45%),
      radial-gradient(ellipse at 20% 75%, rgba(60,60,60,0.40) 0, transparent 55%),
      radial-gradient(ellipse at 60% 85%, rgba(55,55,55,0.35) 0, transparent 40%),
      linear-gradient(165deg, var(--flyer-grey) 0%, var(--flyer-mid) 45%, var(--flyer-black) 100%);
  }
  .flyer__rose {
    position: absolute;
    left: 325px;
    top: 78px;
    width: 130px;
    height: 120px;
    border-radius: 50%;
    background: radial-gradient(circle at 50% 50%, var(--rose-red) 0, #8e0a12 50%, rgba(94,2,8,0) 72%);
  }
  .flyer__title {
    position: absolute;
    left: 0;
    right: 0;
    top: 200px;
    margin: 0;
    text-align: center;
    font-family: "Anton", "Impact", sans-serif;
    font-weight: 400;
    font-size: 160px;
    line-height: 1;
    letter-spacing: 3px;
    color: var(--gold);
  }
  .flyer__subtitle {
    position: absolute;
    left: 0;
    right: 0;
    top: 420px;
    margin: 0;
    text-align: center;
    font-family: "Kelly Slab", serif;
    font-weight: 400;
    font-size: 60px;
    line-height: 1.1;
    color: var(--rose-red);
    letter-spacing: 1px;
  }
  .flyer__details {
    position: absolute;
    left: 60px;
    bottom: 80px;
    margin: 0;
    font-family: "Share Tech Mono", monospace;
    font-variant: small-caps;
    font-size: 25px;
    line-height: 1.5;
    color: var(--gold);
  }
  .flyer__details span { display: block; }
  .flyer__details .indent { padding-left: 80px; }
</style>
</head>
<body>
  <article class="flyer">
    <div class="flyer__backdrop-photo" role="img" aria-label="Dark textured photograph of DJ turntables with soft bokeh lights"></div>
    <div class="flyer__rose" role="img" aria-label="Red rose with green leaves"></div>
    <h1 class="flyer__title">VELANZA</h1>
    <p class="flyer__subtitle">REGGAETON<br>NIGHT</p>
    <p class="flyer__details">
      <span>Date: December 16 2017. | Time: 7pm to 3am.</span>
      <span class="indent">Location: Central London</span>
    </p>
  </article>
</body>
</html>
```